Builders Worksite Corflute Outdoor Sign

We are a building company who are just branching out into new construction. How first new build is our own home which was designed by us and a local architect. We are proud and want to create more advertisement around our business.

We need a corflute sign that can staked outside the construction site and can be seen by people passing by.
Updates

Can we please make the company name and logo bigger (Tidewater Ridge Homes) This needs to be the focus. Can we please replace 'Manu' with 'Contact Us on 021-574-3619'

Target Market(s)

Home owners and people wishing to build on lifestyle blocks in New Zealand.

Font styles to use
Sans Serif

Requirements
Must have
• It needs to feature our:
Logo
Company name
Contact name and number - Manu - 0215743619
Landscape NOT portrait.

```html
<!DOCTYPE html>
<html lang="en">
<head>
<meta charset="utf-8">
<title>Tidewater Ridge Homes – Site Sign</title>
<link rel="stylesheet" href="https://fonts.googleapis.com/css2?family=Jost:wght@400;500&family=Montserrat:wght@700&display=swap">
<style>
  :root {
    --navy: #171f2f;
    --silver-edge: #a9a9a9;
    --silver-mid: #d2d2d2;
    --silver-light: #d9d9d9;
    --frame: #b8b8b8;
    --gold-top: #f7c816;
    --gold-bottom: #cf9a2b;
    --white: #ffffff;
    --backdrop: #e4e4e4;
  }
  * { margin: 0; padding: 0; box-sizing: border-box; }
  html, body {
    width: 1200px;
    height: 1200px;
    overflow: hidden;
    background: var(--backdrop);
  }
  .sign {
    position: absolute;
    left: 0;
    top: 200px;
    width: 1200px;
    height: 800px;
    background: var(--frame);
  }
  .sign-face {
    position: absolute;
    left: 15px;
    top: 15px;
    right: 15px;
    bottom: 15px;
    border: 2px solid var(--navy);
    background: linear-gradient(90deg, var(--silver-edge) 0%, var(--silver-mid) 30%, var(--silver-light) 50%, var(--silver-mid) 70%, var(--silver-edge) 100%);
  }
  .brand-dot {
    position: absolute;
    left: 520px;
    top: 45px;
    width: 160px;
    height: 160px;
    border-radius: 50%;
    background: var(--gold-top);
  }
  .brand-name {
    position: absolute;
    left: 0;
    width: 1200px;
    text-align: center;
    font-family: "Jost", sans-serif;
    font-weight: 400;
    color: var(--navy);
    line-height: 1;
  }
  .brand-name--main {
    top: 300px;
    font-size: 100px;
    letter-spacing: 1px;
  }
  .brand-name--sub {
    top: 440px;
    font-size: 64px;
    letter-spacing: 40px;
    padding-left: 40px;
  }
  .contact-band {
    position: absolute;
    left: 15px;
    right: 15px;
    top: 615px;
    height: 168px;
    background: var(--navy);
  }
  .contact-label {
    position: absolute;
    left: 393px;
    top: 570px;
    width: 415px;
    height: 62px;
    border: 3px solid #d8d8d8;
    border-radius: 8px;
    background: linear-gradient(180deg, var(--gold-top), var(--gold-bottom));
    font-family: "Jost", sans-serif;
    font-weight: 500;
    font-size: 46px;
    line-height: 56px;
    text-align: center;
    color: var(--navy);
    letter-spacing: 1px;
    z-index: 2;
  }
  .contact-phone {
    position: absolute;
    left: 0;
    top: 640px;
    width: 1200px;
    text-align: center;
    font-family: "Montserrat", sans-serif;
    font-weight: 700;
    font-size: 136px;
    line-height: 120px;
    letter-spacing: 6px;
    color: var(--white);
  }
</style>
</head>
<body>
  <div class="sign">
    <div class="sign-face"></div>
    <div class="brand-dot"></div>
    <div class="brand-name brand-name--main">TIDEWATER RIDGE</div>
    <div class="brand-name brand-name--sub">HOMES</div>
    <div class="contact-band"></div>
    <div class="contact-label">CONTACT US ON</div>
    <div class="contact-phone">021-574-3619</div>
  </div>
</body>
</html>
```